Edgy book cover - contemporary fiction

A book cover design for a first-time author. The book is being self-published, but needs to stand out as a quality product amongst a huge number of self-published titles hitting the market.

About the book
“Dust on the Staircase” is a collection of eleven fictional short stories, set in the the turbulent economic times of The Great Recession (Or the Global Financial Crisis). The stories are about ordinary people and their struggles and hopes, as they cope with the circumstances that are dealt them: losing their jobs and homes, helping friends in trouble, making their own success, having to move across town or across the world to survive, having to go back to work after losing their retirement savings.

The book is being published as an e-book only at this stage. The graphic will be viewed as an icon on the rivermart glowpad store (and similar stores such as Quince pagevault), and as a larger image on the book's own page. In future, the cover may be used in a print version.

I expect to be challenged and stimulated along the way as I don’t have a firm view of what the final cover will look like – it really is up to you to wow me. I value your time and as such I will commit to giving each designer feedback.

Required Deliverables

Although you need only submit the book cover at the design stage the required project deliverables are:
- Book Front Cover - colour. Main focus
- Other versions once finalised:
- Colour image image 928px wide by 1250px high, at 150ppi,
- B&W image 96ppi B/W, and it will resize automatically to 600px by 800px, which is perfect for the inside Glowpad cover.
- 6 by 4 inch postcards and A4 posters for promotional purposes
- Final tag-line applied to all of the above
- Front, back and spine book cover design for future printing of physical book, size 5.25 inches by 8 inches. Rivermart Presswell template available when number of pages has been finalised.
- At least 2 iterations of the winning design
Updates

Target Market(s)

The target for this book is a broad, educated middle-class audience, say over age 30, for whom home, mortgage and job are real concerns.

Industry/Entity Type

Printing

Requirements
Must have
• The cover needs to be edgy but not overdone. Less is more in this case. Think about the target audience and their tastes. I think the title gives lots of creative possibility, so please be creative and clever. I’d like people to look at the cover and think “Cool/Clever cover – I’d better read this”. Be original yet keep the end product accessible.

There will be a tag-line on the cover somewhere. Where you locate it is up to you, but you need to leave space for it. For the time being please use the text “Tales of Uneasy Seasons ” – but this may change by the end of the project.

The following text of title, tagline and author

Dust on the Staircase
Tales of Uneasy Seasons
Lena Pritchett

Purely as guidance to my taste, some book covers I like are:

http://lnkr.zq/kaorm
http://lnkr.zq/5193e
http://lnkr.zq/pbelf
http://lnkr.zq/r4ktj
http://lnkr.zq/8um32
http://lnkr.zq/hxona
Should not have
• Please avoid clichés and being “overly busy”. Although the book is to be self published on a low budget it shouldn’t look like that. If the cover would look right on a popular mass fiction title then it is probably not right for me.

The design should not use a cliched "happy families" house image.

It needs not to look like it's based on a book cover template from a self-publishing house.

Some examples of book covers I don’t like are :

http://lnkr.zq/7ke2p
http://lnkr.zq/4rfyb
http://lnkr.zq/j512s
http://lnkr.zq/muf48
http://lnkr.zq/eb9ox

```html
<!DOCTYPE html>
<html lang="en">
<head>
<meta charset="utf-8">
<title>Dust on the Staircase – Cover Options</title>
<link href="https://fonts.googleapis.com/css2?family=Jost:wght@200;300&display=swap" rel="stylesheet">
<style>
  :root {
    --sheet: #ffffff;
    --ink: #1a1a1a;
    --ink-soft: #4a4a4a;
    --frame: #3a3a3a;
    --label: #222222;
  }
  * { margin: 0; padding: 0; box-sizing: border-box; }
  html, body {
    width: 853px;
    height: 1200px;
    overflow: hidden;
    background: var(--sheet);
  }
  .sheet {
    position: relative;
    width: 853px;
    height: 1200px;
    background: var(--sheet);
    font-family: "Jost", "Futura", sans-serif;
  }
  .cover {
    position: absolute;
    width: 335px;
    height: 516px;
    border: 1px solid var(--frame);
    background: var(--sheet);
    overflow: hidden;
  }
  .cover--a { left: 69px;  top: 40px; }
  .cover--b { left: 445px; top: 40px; }
  .cover--c { left: 69px;  top: 598px; }
  .cover--d { left: 445px; top: 598px; }

  .cover__art {
    position: absolute;
    left: 0;
    top: 0;
    width: 335px;
    height: 516px;
  }
  .cover__author {
    position: absolute;
    left: 21px;
    top: 14px;
    font-weight: 200;
    font-size: 39px;
    letter-spacing: 3.5px;
    color: var(--ink-soft);
    white-space: nowrap;
  }
  .cover__title {
    position: absolute;
    left: 20px;
    top: 64px;
    font-weight: 200;
    font-size: 49px;
    line-height: 1;
    letter-spacing: 0;
    color: var(--ink);
    text-transform: uppercase;
    white-space: nowrap;
  }
  .cover__tagline {
    position: absolute;
    left: 22px;
    top: 206px;
    font-weight: 200;
    font-size: 26px;
    color: var(--ink-soft);
    white-space: nowrap;
  }
  .option-label {
    position: absolute;
    font-size: 11px;
    font-weight: 300;
    color: var(--label);
  }
</style>
</head>
<body>
<main class="sheet">

  <section class="cover cover--a">
    <svg class="cover__art" viewBox="0 0 335 516" role="img" aria-label="Aerial photograph of a curving suburban housing estate in olive sepia tones, torn away from the white cover">
      <defs>
        <linearGradient id="tone-a" x1="0" y1="1" x2="1" y2="0">
          <stop offset="0" stop-color="#5d5c36"/>
          <stop offset="0.55" stop-color="#8a8858"/>
          <stop offset="1" stop-color="#a9a77b"/>
        </linearGradient>
      </defs>
      <path fill="url(#tone-a)" d="M335,163 L326,168 L322,186 L310,196 L304,214 L292,222 L286,240 L268,248 L262,262 L246,270 L236,290 L220,298 L208,318 L196,326 L184,346 L166,356 L152,372 L130,380 L118,398 L112,418 L96,432 L92,452 L84,470 L86,492 L80,516 L335,516 Z"/>
      <path fill="#5d5c36" d="M118,360 q-8,-4 -6,4 q6,4 14,2 z"/>
    </svg>
    <p class="cover__author">Lena Pritchett</p>
    <h1 class="cover__title">Dust on the<br>Staircase</h1>
    <p class="cover__tagline">Tales of Uneasy Seasons</p>
  </section>
  <span class="option-label" style="left:396px; top:566px;">a</span>

  <section class="cover cover--b">
    <svg class="cover__art" viewBox="0 0 335 516" role="img" aria-label="Close aerial photograph of suburban rooftops, lawns, a pool and a street in full colour, torn away from the white cover">
      <defs>
        <linearGradient id="tone-b" x1="0" y1="0" x2="0" y2="1">
          <stop offset="0" stop-color="#6f5a4a"/>
          <stop offset="0.35" stop-color="#5f7044"/>
          <stop offset="0.6" stop-color="#8c8c8c"/>
          <stop offset="1" stop-color="#7a5444"/>
        </linearGradient>
      </defs>
      <path fill="url(#tone-b)" d="M335,163 L326,170 L322,186 L300,196 L296,214 L286,232 L294,252 L278,262 L262,272 L246,288 L230,302 L218,322 L196,334 L170,346 L150,360 L134,364 L128,380 L122,400 L128,422 L118,440 L114,462 L104,480 L108,498 L104,516 L335,516 Z"/>
      <path fill="#4d4a40" d="M128,348 q-8,-4 -6,4 q6,4 14,2 z"/>
    </svg>
    <p class="cover__author">Lena Pritchett</p>
    <h1 class="cover__title">Dust on the<br>Staircase</h1>
    <p class="cover__tagline">Tales of Uneasy Seasons</p>
  </section>
  <span class="option-label" style="left:772px; top:566px;">b</span>

  <section class="cover cover--c">
    <svg class="cover__art" viewBox="0 0 335 516" role="img" aria-label="Aerial photograph of a modern cul-de-sac with grey roads, gardens and terraced houses, torn away from the white cover">
      <defs>
        <linearGradient id="tone-c" x1="0" y1="1" x2="1" y2="0">
          <stop offset="0" stop-color="#8e9aa0"/>
          <stop offset="0.45" stop-color="#6f8a4e"/>
          <stop offset="1" stop-color="#8f98a0"/>
        </linearGradient>
      </defs>
      <path fill="url(#tone-c)" d="M335,162 L322,168 L312,178 L300,176 L290,190 L292,214 L282,236 L270,244 L262,262 L250,284 L232,296 L212,300 L196,308 L170,314 L150,330 L136,352 L130,370 L116,380 L114,402 L108,428 L118,452 L108,476 L114,498 L108,516 L335,516 Z"/>
      <path fill="#5f6a5a" d="M116,360 q-8,-4 -6,4 q6,4 14,2 z"/>
    </svg>
    <p class="cover__author">Lena Pritchett</p>
    <h1 class="cover__title">Dust on the<br>Staircase</h1>
    <p class="cover__tagline">Tales of Uneasy Seasons</p>
  </section>
  <span class="option-label" style="left:394px; top:1123px;">c</span>

  <section class="cover cover--d">
    <svg class="cover__art" viewBox="0 0 335 516" role="img" aria-label="Oblique aerial photograph of a dense older suburb with red-tiled roofs and trees, torn away from the white cover">
      <defs>
        <linearGradient id="tone-d" x1="0" y1="1" x2="1" y2="0">
          <stop offset="0" stop-color="#6d4232"/>
          <stop offset="0.4" stop-color="#5c5a3c"/>
          <stop offset="0.75" stop-color="#a4664a"/>
          <stop offset="1" stop-color="#c9a48a"/>
        </linearGradient>
      </defs>
      <path fill="url(#tone-d)" d="M335,162 L324,172 L318,192 L302,202 L296,222 L284,234 L290,250 L274,262 L270,282 L252,298 L246,316 L228,330 L206,336 L190,350 L170,356 L146,366 L134,380 L122,394 L124,412 L112,430 L104,452 L108,474 L100,492 L96,516 L335,516 Z"/>
      <path fill="#4a3a2e" d="M126,356 q-8,-4 -6,4 q6,4 14,2 z"/>
    </svg>
    <p class="cover__author">Lena Pritchett</p>
    <h1 class="cover__title">Dust on the<br>Staircase</h1>
    <p class="cover__tagline">Tales of Uneasy Seasons</p>
  </section>
  <span class="option-label" style="left:772px; top:1123px;">d</span>

</main>
</body>
</html>
```